needing web design for aerial and satellite installation comapny

We need our website designing, it needs to be professional and look creative,
We are a aerial and satellite company called Kestrel Mend & Reach ()
I like this site design also some of the following maybe:

https://www.skywirelo.co.uk/

http://holdmoor.co.uk/

http://quillnine-guard.co.uk/portfolio/zmp-holdmoor/

The design will require coding once the design is complete, i haven't paid for this yet as i want to be sure the design is good before i commit.

The template needs to look professional and look like one of the leading companies.
The site will consist of all the features this site has https://www.skywirelo.co.uk/

I like a modern design with the latest technology.

Target Market(s)

tv aerial satellite installation

Industry/Entity Type

Satellite Tv

Number of Pages Required

3 page

Font styles to use
Sans Serif

Colors

Designer to choose colors to be used in the design.

Requirements
Must have
• eb Contest Brief We need our website designing, it needs to be professional and look creative,
• We are a aerial and satellite company called Kestrel Mend Reach ()
• I like this site design also some of the following maybe:
• https://www.skywirelo.co.uk/
• http://holdmoor.co.uk/
• http://quillnine-guard.co.uk/portfolio/zmp-holdmoor/
• The design will require coding once the design is complete, i haven't paid for this yet as i want to be sure the design is good before i commit.
• The template needs to look professional and look like one of the leading companies.
• The site will consist of all the features this site has https://www.skywirelo.co.uk/
• I like a modern design with the latest technology.
Nice to have
• http://holdmoor.co.uk/
Should not have
• poor design

```html
<!DOCTYPE html>
<html lang="en">
<head>
<meta charset="utf-8">
<title>Kestrel Mend &amp; Reach</title>
<link rel="stylesheet" href="https://fonts.googleapis.com/css2?family=Hind:wght@400;500&family=Raleway:wght@400;500&display=swap">
<style>
:root{
  --ink:#0a0e1f;
  --navy:#1e2a44;
  --orange:#f39200;
  --text:#2b2f3a;
  --muted:#7b7f88;
  --page:#f6f7f9;
  --white:#ffffff;
  --line:#e3e5ea;
}
*{box-sizing:border-box;margin:0;padding:0}
html,body{width:1200px;height:1200px;overflow:hidden;background:var(--page)}
body{position:relative;font-family:"Raleway",sans-serif;color:var(--text)}
.topbar{position:absolute;left:0;top:0;width:1200px;height:29px;background:var(--ink)}
.header{position:absolute;left:0;top:29px;width:1200px;height:85px;background:var(--white)}
.brand{position:absolute;left:228px;top:28px;width:130px;text-align:center;font-family:"Hind",sans-serif;font-weight:500;font-size:14px;letter-spacing:.5px;color:var(--ink);line-height:1.2}
.nav{position:absolute;left:443px;top:30px;display:flex;gap:0;font-family:"Hind",sans-serif;font-size:12px;letter-spacing:.6px;color:var(--ink)}
.nav a{display:block;padding:3px 8px 2px;margin-right:9px;text-decoration:none;color:inherit;line-height:16px}
.nav a.active{background:var(--orange);color:var(--white)}
.hero{position:absolute;left:0;top:114px;width:1200px;height:545px;background:linear-gradient(160deg,#1a2845 0%,#24365a 40%,#3a4c6c 70%,#4a5a75 100%)}
.hero-title{position:absolute;left:0;top:222px;width:1160px;text-align:center;font-family:"Hind",sans-serif;font-weight:400;font-size:40px;color:var(--white)}
.hero-sub{position:absolute;left:0;top:281px;width:1160px;text-align:center;font-family:"Hind",sans-serif;font-weight:500;font-size:13px;letter-spacing:.6px;color:var(--white)}
.hero-btn{position:absolute;left:522px;top:330px}
.services{position:absolute;left:120px;top:610px;width:960px;height:106px;background:var(--white);display:flex;box-shadow:0 2px 6px rgba(0,0,0,.06)}
.service{position:relative;border-right:1px solid var(--line);padding-top:9px}
.service:last-child{border-right:none}
.service h3{font-family:"Hind",sans-serif;font-weight:400;font-size:11.5px;letter-spacing:.4px;text-align:center;color:var(--ink)}
.service.current h3{color:var(--orange)}
.service p{position:absolute;top:29px;font-size:10.3px;line-height:16px;color:var(--muted)}
.trust{position:absolute;left:121px;top:744px;width:245px;height:37px;background:var(--navy);color:var(--white);font-family:"Hind",sans-serif;font-weight:500;font-size:11.5px;letter-spacing:.3px;text-align:center;line-height:39px}
.intro{position:absolute;left:121px;top:800px;width:640px;font-size:10.4px;line-height:16px;color:var(--text)}
.card{position:absolute;width:296px;height:300px}
.card .photo{position:absolute;left:0;top:0;width:296px;height:252px;clip-path:polygon(0 0,100% 0,100% 83%,0 100%)}
.card .panel{position:absolute;left:41px;top:124px;width:221px;height:166px;background:var(--white);clip-path:polygon(0 25%,100% 0,100% 100%,0 100%)}
.card h4{position:absolute;left:33px;top:65px;font-family:"Hind",sans-serif;font-weight:400;font-size:21px;color:var(--navy);padding-left:13px;line-height:20px}
.card h4::before{content:"";position:absolute;left:0;top:1px;width:4px;height:16px;background:var(--orange)}
.card p{position:absolute;left:32px;top:93px;font-family:"Hind",sans-serif;font-size:10.3px;line-height:19px;color:var(--text)}
.card .more{position:absolute;left:30px;top:142px;font-family:"Hind",sans-serif;font-size:10.3px;color:var(--ink);letter-spacing:.2px}
</style>
</head>
<body>
<div class="topbar"></div>
<header class="header">
  <div class="brand">Kestrel Mend &amp; Reach</div>
  <nav class="nav">
    <a class="active" href="#">HOME</a>
    <a href="#">ABOUT US</a>
    <a href="#">AERIALS</a>
    <a href="#">SATELLITE</a>
    <a href="#">SYSTEM INTERGATION</a>
    <a href="#">AREAS</a>
    <a href="#">CONTACT US</a>
  </nav>
</header>

<section class="hero" role="img" aria-label="Silhouette of an installer fitting a satellite dish against a dusk sky">
  <h1 class="hero-title">Kestrel Mend &amp; Reach</h1>
  <p class="hero-sub">Independent TV Aerial, Satellite &amp; CCTV Installers</p>
  <svg class="hero-btn" width="149" height="29" viewBox="0 0 149 29">
    <rect x="0" y="0" width="149" height="29" fill="#1e2a44"/>
    <polygon points="0,0 104,0 97,29 0,29" fill="#f39200"/>
    <text x="51" y="19.5" text-anchor="middle" font-family="Hind, sans-serif" font-size="13.5" fill="#ffffff" letter-spacing=".5">click here</text>
    <path d="M120 14.5h14M129 10l5 4.5-5 4.5" stroke="#ffffff" stroke-width="1.2" fill="none"/>
  </svg>
</section>

<section class="services">
  <div class="service" style="width:242px"><h3>Smart Home System</h3><p style="left:49px">We are familiar with the latest<br>Smart Home product<br>controllers and app devices.</p></div>
  <div class="service current" style="width:237px"><h3>TV Aerial Services</h3><p style="left:47px">We offer a range of Aerial Services<br>including: TV Loft Aerials - Radio<br>Aerials &nbsp;and more.</p></div>
  <div class="service" style="width:240px"><h3>Orbit Satellite TV</h3><p style="left:40px">We provide full Orbit Services, OpenSat<br>Installations, European Satellite<br>Systems, New Satellite Extension<br>Points.</p></div>
  <div class="service" style="width:241px"><h3>Sound &amp; Vision</h3><p style="left:50px">We are also specialists in:<br>Multi-Room Audio, Home Cinema<br>Systems, Sonara Systems and other<br>services.</p></div>
</section>

<div class="trust">Trust &amp; Reliability</div>
<p class="intro">Lorem ipsum dolor sit amet, consetetur sadipscing elitr, sed diam nonumy eirmod tempor invidunt ut labore et dolore magna aliquyam erat, sed diam voluptua. At vero eos et accusam et justo duo dolores et ea rebum.</p>

<article class="card" style="left:122px;top:884px">
  <div class="photo" role="img" aria-label="Engineer on a ladder fitting an aerial to a brick wall" style="background:linear-gradient(135deg,#c9cfd8 0%,#a58a6c 45%,#8a6c50 100%)"></div>
  <div class="panel"><h4>Renovation</h4><p>Lorem ipsum dolor sit amet,<br>consetetur sadipscing elitr, sed</p><span class="more">READ MORE</span></div>
</article>

<article class="card" style="left:448px;top:889px">
  <div class="photo" role="img" aria-label="Man on a sofa holding a remote in front of a wall-mounted television" style="background:linear-gradient(135deg,#d8d2cb 0%,#a89a8c 50%,#2e3550 100%)"></div>
  <div class="panel"><h4>Repair</h4><p>Lorem ipsum dolor sit amet,<br>consetetur sadipscing elitr, sed</p><span class="more">READ MORE</span></div>
</article>

<article class="card" style="left:784px;top:886px">
  <div class="photo" role="img" aria-label="Satellite dishes on a rooftop under a blue sky" style="background:linear-gradient(160deg,#3f7fc4 0%,#4c88c8 55%,#7d7670 100%)"></div>
  <div class="panel"><h4>Consulting</h4><p>Lorem ipsum dolor sit amet,<br>consetetur sadipscing elitr, sed</p><span class="more">READ MORE</span></div>
</article>
</body>
</html>
```